Business Card for new Architectural Firm

I intend to practice in a rural mountain community in upstate NY, focusing on residential and light commercial projects, including second home / vacation properties. I wish to convey a feeling of rural outdoorsy modernity.

Color is important - bold and urbane. Secondary or tertiary colors preferred.

Font is important, idiosyncratic is ok

Optionally, I may choose to use the name Brackenfold Studio. If used as part of your design, all of the Must Haves are still required.

Images uploaded are logos I like

Industry/Entity Type

Residential

Contact Information for Business Card

Caldwell Prusinski
Architect (This word should stand alone or be associated with my name - not license number)
NY License No. 582163
caldwell@designcpx.com
607 394 2858

Font styles to use
Sans Serif
Decorative

Requirements
Must have
• Whatever files I need to best utilize your design
• PDF
• JPG
• EPS
• Vectorwhatsit
Nice to have
• Logo or element that can be incorporated into other print material.
• Could be a font based card
Should not have
• no clip art
• No templates
• no floor plans
• no building photographs

```html
<!DOCTYPE html>
<html lang="en">
<head>
<meta charset="utf-8">
<title>Brackenfold Studio – Business Card</title>
<link href="https://fonts.googleapis.com/css2?family=Questrial&display=swap" rel="stylesheet">
<style>
  :root {
    --stage: #1c1c1e;
    --card: #5e2f2f;
    --card-shade: #4f2626;
    --accent: #e5531c;
    --ink: #ffffff;
    --ink-soft: #e9dcdc;
  }
  * { box-sizing: border-box; margin: 0; padding: 0; }
  html, body { width: 1200px; height: 1000px; overflow: hidden; }
  body {
    background: var(--stage);
    font-family: "Questrial", "Century Gothic", sans-serif;
    display: flex;
    flex-direction: column;
    align-items: center;
    justify-content: center;
    gap: 70px;
  }
  .card {
    position: relative;
    width: 700px;
    height: 400px;
    background: var(--card);
    border-radius: 14px;
    overflow: hidden;
    box-shadow: 0 10px 30px rgba(0,0,0,.45);
  }
  .accent-band {
    position: absolute;
    top: 0; bottom: 0;
    width: 18px;
    background: var(--accent);
  }
  .card--front .accent-band { left: 0; }
  .card--back .accent-band { right: 0; }

  .brand {
    position: absolute;
    left: 70px;
    top: 150px;
    width: 260px;
    text-align: center;
    color: var(--ink);
    font-size: 30px;
    letter-spacing: 1px;
    line-height: 1.2;
  }
  .divider {
    position: absolute;
    left: 360px;
    top: 50px;
    width: 2px;
    height: 300px;
    background: var(--ink);
  }
  .identity {
    position: absolute;
    left: 400px;
    top: 70px;
    color: var(--ink-soft);
  }
  .identity__name { font-size: 26px; letter-spacing: .5px; }
  .identity__role {
    margin-top: 4px;
    margin-left: 40px;
    font-size: 14px;
    letter-spacing: 4px;
  }
  .contacts {
    position: absolute;
    left: 400px;
    top: 230px;
    list-style: none;
    color: var(--ink-soft);
    font-size: 15px;
  }
  .contacts li {
    display: flex;
    align-items: center;
    gap: 10px;
    height: 28px;
  }
  .contacts svg { width: 16px; height: 16px; fill: var(--ink); flex: none; }

  .brand--embossed {
    left: 0; right: 0;
    top: 175px;
    width: auto;
    color: var(--card-shade);
    font-size: 34px;
  }
</style>
</head>
<body>
  <section class="card card--front" aria-label="Business card front">
    <div class="accent-band"></div>
    <div class="brand">Brackenfold Studio</div>
    <div class="divider"></div>
    <div class="identity">
      <div class="identity__name">Caldwell Prusinski</div>
      <div class="identity__role">ARCHITECT</div>
    </div>
    <ul class="contacts">
      <li>
        <svg viewBox="0 0 16 16" aria-hidden="true"><path d="M1 3h14v10H1z M2 4l6 5 6-5" fill="none" stroke="#fff" stroke-width="1.4"/></svg>
        caldwell@designcpx.com
      </li>
      <li>
        <svg viewBox="0 0 16 16" aria-hidden="true"><path d="M4 1l3 3-2 2c1 2 3 4 5 5l2-2 3 3-2 3C7 14 2 9 1 3z"/></svg>
        607 394 2858
      </li>
      <li>
        <svg viewBox="0 0 16 16" aria-hidden="true"><circle cx="8" cy="8" r="6.5" fill="none" stroke="#fff" stroke-width="1.5"/><path d="M5 8l2 2 4-4" fill="none" stroke="#fff" stroke-width="1.5"/></svg>
        NY License No. 582163
      </li>
    </ul>
  </section>

  <section class="card card--back" aria-label="Business card back">
    <div class="accent-band"></div>
    <div class="brand brand--embossed">Brackenfold Studio</div>
  </section>
</body>
</html>
```